Holvery Real Estate Management Consulting

To design a high end company profile that inspires confidence in high net worth individuals and similar clients. The profile to include real estate images, preferably real images. The firm is a Zambian firm and has its target to be comparable to Tesk & Company, Parlowe & Company, Wilder Osten, Lun dorv pelsin wilder osten, TLAV Real estate company as such.

Target Market(s)

Real estate clients such as high net worth individuals, private and public companies, government and international agencies, banks and insurance companies, trusts and pension funds and individual investors. the sub target market group being developers, planners, financiers, market analysts, designers, economists, engineers, architects, construction managers, quantity surveyors and public officials and others

Colors

Designer to choose colors to be used in the design.

Requirements
Must have
• Company logo

```html
<!DOCTYPE html>
<html lang="en">
<head>
<meta charset="utf-8">
<title>Holvery Real Estate – Company Profile</title>
<link href="https://fonts.googleapis.com/css2?family=Open+Sans:wght@300;400;600;700&display=swap" rel="stylesheet">
<style>
  :root {
    --blue: #2f4ba1;
    --grey: #7d7d7d;
    --grey-text: #8a8a8a;
    --dark-text: #5e5e5e;
    --paper: #ffffff;
    --backdrop: #dedfe2;
  }
  * { margin: 0; padding: 0; box-sizing: border-box; }
  html, body { width: 970px; height: 1200px; overflow: hidden; background: var(--backdrop); }
  body { font-family: "Open Sans", Arial, sans-serif; }
  .artboard { position: absolute; left: 0; top: 0; width: 1212px; height: 1500px; transform: scale(0.8); transform-origin: 0 0; }
  .page { position: absolute; width: 483px; height: 683px; background: var(--paper); overflow: hidden; }
  .page > svg.shapes { position: absolute; left: 0; top: 0; width: 483px; height: 683px; }
  .abs { position: absolute; }
  .rule { position: absolute; height: 2px; background: var(--blue); }
  .rule.grey { background: var(--grey); height: 1px; }

  /* back cover */
  .back-cover { left: 58px; top: 29px; }
  .contact-title { left: 65px; top: 56px; font-size: 25px; font-weight: 600; color: #fff; letter-spacing: -.3px; }
  .contact-row { position: absolute; left: 65px; display: flex; gap: 11px; color: #fff; font-size: 8px; line-height: 10.2px; }
  .contact-row svg { flex: 0 0 16px; width: 16px; height: 14px; }
  .slogan { left: 218px; top: 352px; font-size: 26px; line-height: 32px; font-weight: 600; }
  .slogan .accent { color: var(--blue); display: block; }
  .slogan .soft { color: var(--grey); display: block; padding-left: 15px; }

  /* front cover */
  .front-cover { left: 667px; top: 29px; }
  .brand { right: 39px; top: 58px; text-align: right; }
  .brand-name { display: flex; align-items: center; justify-content: flex-end; gap: 7px; font-size: 15px; font-weight: 700; color: var(--blue); letter-spacing: .4px; }
  .brand-name::before { content: ""; width: 12px; height: 12px; background: var(--blue); }
  .brand-tag { font-size: 7px; color: var(--grey); letter-spacing: .3px; margin-top: 1px; }
  .cover-claim { right: 30px; top: 493px; text-align: right; color: var(--grey); font-weight: 600; }
  .cover-claim .c1 { font-size: 16px; line-height: 24px; }
  .cover-claim .c2 { font-size: 22px; line-height: 28px; color: var(--blue); font-weight: 700; }
  .cover-claim .c3 { font-size: 20px; line-height: 26px; }
  .website { left: 48px; top: 612px; font-size: 12.5px; font-weight: 700; color: var(--blue); }

  /* vision page */
  .vision-page { left: 58px; top: 794px; }
  .section-title { font-size: 20px; color: var(--grey); font-weight: 300; white-space: nowrap; }
  .section-title b { color: var(--blue); font-weight: 700; }
  .service-list { left: 31px; top: 456px; list-style: none; }
  .service-list li { position: absolute; left: 0; display: flex; align-items: center; gap: 14px; width: 220px; font-size: 11.5px; line-height: 15px; color: var(--grey-text); text-transform: uppercase; }
  .service-icon { width: 30px; height: 30px; background: var(--blue); flex: 0 0 30px; }
  .vision-head { position: absolute; left: 255px; font-size: 11.5px; font-weight: 700; color: var(--blue); display: flex; align-items: center; gap: 7px; }
  .vision-head::before { content: ""; border-left: 9px solid var(--grey); border-top: 5.5px solid transparent; border-bottom: 5.5px solid transparent; }
  .body-copy { position: absolute; font-size: 8.3px; line-height: 12.8px; color: var(--grey-text); }

  /* about page */
  .about-page { left: 667px; top: 794px; }
  .inspire-box { left: 30px; top: 32px; width: 201px; height: 34px; background: #fff; display: flex; align-items: center; justify-content: center; font-size: 21px; font-weight: 300; color: var(--blue); }
  .inspire-box b { font-weight: 700; margin-right: 6px; }
  .who-title { left: 30px; top: 113px; font-size: 20px; color: #fff; font-weight: 300; }
  .who-title b { font-weight: 700; }
  .who-rule { left: 30px; top: 141px; width: 54px; height: 1px; background: #fff; }
  .who-copy { left: 30px; top: 156px; width: 166px; font-size: 10px; line-height: 12.4px; color: #fff; text-align: justify; }
  .who-copy b { font-weight: 600; }
  .solutions { left: 258px; top: 75px; width: 205px; list-style: none; }
  .solutions li { position: relative; padding-left: 12px; font-size: 8.3px; line-height: 12.8px; color: var(--grey-text); margin-bottom: 11px; }
  .solutions li::before { content: ""; position: absolute; left: 0; top: 3px; border-left: 6px solid var(--blue); border-top: 3.5px solid transparent; border-bottom: 3.5px solid transparent; }
  .principle { position: absolute; font-size: 13px; color: var(--blue); display: flex; align-items: center; gap: 8px; white-space: nowrap; }
  .principle::before { content: ""; border-left: 9px solid var(--grey); border-top: 5.5px solid transparent; border-bottom: 5.5px solid transparent; }
</style>
</head>
<body>
<div class="artboard">

  <!-- Back cover: contact -->
  <section class="page back-cover">
    <svg class="shapes" viewBox="0 0 483 683">
      <defs>
        <linearGradient id="estateA" x1="0" y1="0" x2="0" y2="1">
          <stop offset="0" stop-color="#7fb2e0"/><stop offset=".45" stop-color="#c9dcec"/><stop offset=".62" stop-color="#4d4f57"/><stop offset=".85" stop-color="#7da24c"/><stop offset="1" stop-color="#d9d6cd"/>
        </linearGradient>
      </defs>
      <polygon role="img" aria-label="Photo of a stone manor house with balustrade and lawn" points="0,455 120,388 483,598 483,683 0,683" fill="url(#estateA)"/>
      <polygon points="0,318 37,340 37,431 0,455" fill="var(--blue)"/>
      <polygon points="483,399 312,496 483,600" fill="var(--blue)"/>
      <polygon points="37,0 264,0 264,298 37,431" fill="var(--grey)"/>
    </svg>
    <h2 class="abs contact-title">CONTACT US</h2>
    <div class="rule" style="left:65px;top:89px;width:55px;"></div>
    <div class="contact-row" style="top:111px;">
      <svg viewBox="0 0 16 14"><path d="M6 0a5 5 0 0 1 5 5c0 3.5-5 9-5 9S1 8.5 1 5a5 5 0 0 1 5-5z" fill="#fff"/><circle cx="6" cy="5" r="2" fill="var(--grey)"/></svg>
      <p>Messrs. HRE | Management Consulting<br>Unit 4, Plot NO. 2210<br>Mpande Ridge Road<br>Nsenga, Lusaka Province– Zambia</p>
    </div>
    <div class="contact-row" style="top:163px;">
      <svg viewBox="0 0 16 14"><rect x="0" y="3" width="12" height="8" fill="#fff"/><path d="M0 3l6 5 6-5" stroke="var(--grey)" fill="none" stroke-width="1.2"/></svg>
      <p>info@holverypropertyconsultants.com</p>
    </div>
    <div class="contact-row" style="top:190px;">
      <svg viewBox="0 0 16 14"><path d="M2 1l3 0 1 3-2 1.5a8 8 0 0 0 4 4L9.5 7.5l3 1v3l-1 1C6 12.5 1 7.5 1 2z" fill="#fff"/></svg>
      <p>+260 955 104 218/ 0966 307 415</p>
    </div>
    <h1 class="abs slogan"><span class="accent">ACCELERATE</span><span class="soft">SUCCESS....</span></h1>
  </section>

  <!-- Front cover -->
  <section class="page front-cover">
    <svg class="shapes" viewBox="0 0 483 683">
      <defs>
        <linearGradient id="estateB" x1="0" y1="0" x2="0" y2="1">
          <stop offset="0" stop-color="#5d7fa8"/><stop offset=".3" stop-color="#b9c7cf"/><stop offset=".55" stop-color="#8a7a62"/><stop offset=".75" stop-color="#5f7040"/><stop offset="1" stop-color="#b9aa96"/>
        </linearGradient>
      </defs>
      <polygon role="img" aria-label="Photo of a stone villa with lit doorway, garden steps and olive trees" points="0,0 276,156 483,271 483,321 0,601" fill="url(#estateB)"/>
      <polygon points="0,0 56,0 276,126 276,156" fill="var(--blue)"/>
      <polygon points="483,321 483,366 210,514 210,479" fill="var(--blue)"/>
      <polygon points="353,612 413,612 403,632 343,632" fill="var(--grey)"/>
      <polygon points="403,612 483,612 483,632 393,632" fill="var(--blue)"/>
    </svg>
    <div class="abs brand">
      <div class="brand-name">HOLVERY REAL ESTATE</div>
      <div class="brand-tag">REGISTERED PROPERTY VALUATION SURVEYORS</div>
    </div>
    <h1 class="abs cover-claim">
      <span class="c1" style="display:block">CONFIDENCE</span>
      <span class="c2" style="display:block">THROUGH</span>
      <span class="c3" style="display:block">PROFESSIONALISM</span>
    </h1>
    <p class="abs website">WWW.HOLVERYPROPERTYCONSULTANTS.COM</p>
  </section>

  <!-- Vision page -->
  <section class="page vision-page">
    <svg class="shapes" viewBox="0 0 483 683">
      <defs>
        <linearGradient id="estateC" x1="0" y1="0" x2="0" y2="1">
          <stop offset="0" stop-color="#3f6f9c"/><stop offset=".35" stop-color="#8a5a45"/><stop offset=".6" stop-color="#d8b477"/><stop offset="1" stop-color="#2f3a2a"/>
        </linearGradient>
      </defs>
      <polygon role="img" aria-label="Photo of a tiled-roof mansion lit at dusk among palm trees" points="0,0 483,0 483,141 172,296 0,276" fill="url(#estateC)"/>
      <polygon points="483,141 483,185 215,300 172,296" fill="var(--blue)"/>
      <polygon points="483,185 355,240 483,316" fill="var(--grey)"/>
      <polygon points="0,276 172,296 0,416" fill="var(--blue)"/>
    </svg>

    <h2 class="abs section-title" style="left:29px;top:411px;"><b>SMART</b> MOVE</h2>
    <div class="rule" style="left:29px;top:440px;width:45px;"></div>
    <ul class="abs service-list">
      <li style="top:0;"><span class="service-icon"></span>Services and<br>business lines</li>
      <li style="top:41px;"><span class="service-icon"></span>Advisory services</li>
      <li style="top:84px;"><span class="service-icon"></span>Property consultancy</li>
      <li style="top:125px;"><span class="service-icon"></span>Valuation services</li>
      <li style="top:165px;"><span class="service-icon"></span>Urban planning and<br>development</li>
    </ul>

    <h2 class="abs section-title" style="left:256px;top:322px;"><b>VISION</b></h2>
    <div class="rule grey" style="left:256px;top:351px;width:48px;"></div>
    <h3 class="vision-head" style="top:372px;">CORPORATE RESPONSIBILITY</h3>
    <p class="body-copy" style="left:272px;top:395px;width:186px;">HRE Management Consulting recognises that it has responsibilities to all stakeholders, including the interests of employees and their families; and the need to foster the firms´ business relationships with partners, customers and others to impact local communities and surroundings.</p>
    <h3 class="vision-head" style="top:510px;">COMMUNITY</h3>
    <p class="body-copy" style="left:272px;top:533px;width:180px;">We strive always to be a good neighbor to the surrounding community, and are active in the support of a number of charitable causes.</p>
    <p class="body-copy" style="left:272px;top:596px;width:186px;">Where possible we will encourage and facilitate employee giving, of both their time and money, through a financial and time contribution.</p>
  </section>

  <!-- About page -->
  <section class="page about-page">
    <svg class="shapes" viewBox="0 0 483 683">
      <defs>
        <linearGradient id="estateD" x1="0" y1="0" x2="0" y2="1">
          <stop offset="0" stop-color="#8fb6de"/><stop offset=".4" stop-color="#e4e8ec"/><stop offset=".6" stop-color="#6aa0a0"/><stop offset=".8" stop-color="#5cc8cf"/><stop offset="1" stop-color="#6f8a3e"/>
        </linearGradient>
      </defs>
      <polygon role="img" aria-label="Photo of a resort villa with fountains, pool and sun loungers" points="0,321 231,375 483,620 483,683 0,683" fill="url(#estateD)"/>
      <polygon points="0,0 231,0 231,375 0,321" fill="var(--grey)"/>
      <polygon points="0,321 363,526 363,566 0,356" fill="var(--blue)"/>
    </svg>

    <h2 class="abs inspire-box"><b>INSPIRE</b>VALUE</h2>
    <h2 class="abs who-title"><b>WHO</b> WE ARE</h2>
    <div class="abs who-rule"></div>
    <p class="abs who-copy"><b>HRE | Management Consulting</b> is one of Zambia´s leading professional real estate services firms with an outstanding reputation and has its cornerstone the excellence of its people. Since its inception, the business has continued successfully with a national client base, a number of which have retained our services.</p>

    <h2 class="abs section-title" style="left:258px;top:29px;"><b>OUR</b> SOLUTIONS</h2>
    <div class="rule" style="left:258px;top:56px;width:50px;"></div>
    <ul class="abs solutions">
      <li>As a preferred property firm we continually monitor property value levels and will provide you with an update on market rents, trends and the position of your property in the marketplace.</li>
      <li>We continue to roll out our real estate services for you our clients to benefit from the power of our massive experience and database.</li>
      <li>Our system allows you to save on unnecessary research costs and time of doing new research in the marketplace and all due diligence is done when identifying the interests, benefits and rights being researched.</li>
      <li>We assure our clients and prospective clients that our work is independent, objective and compliant with nationally recognized Laws of the Republic of Zambia.</li>
    </ul>

    <h2 class="abs section-title" style="left:258px;top:334px;line-height:24px;"><b>CLIENT</b><br>SERVICE PRINCIPLES</h2>
    <p class="body-copy" style="left:258px;top:388px;width:205px;">Our values are integral to HRE´S corporate culture and are underpinned by our brand essence alongside our Client Service Principles which include among others:</p>
    <p class="principle" style="left:258px;top:450px;">Professionalism that is unrivalled</p>
    <p class="principle" style="left:314px;top:473px;">Diligence and dignity</p>
    <p class="principle" style="left:391px;top:496px;">Service</p>
    <p class="principle" style="left:399px;top:519px;">Trust</p>
  </section>

</div>
</body>
</html>
```